Business Card Design Project

Use our current logo. Clean design.

Industry/Entity Type

Business

Requirements
Must have
• Marisela DUCRANTE
M. Law
Managing Partner

Velotrana AG
Brunnmattweg 274
CH-3097 Liebefeld

M. +41 79 418 26 97
T. +41 31 742 19 04
F. +41 31 742 19 38

m.ducrante@velotrana.example
www.velotrana.example

```html
<!DOCTYPE html>
<html lang="en">
<head>
<meta charset="utf-8">
<title>Velotrana AG – Business Card</title>
<link href="https://fonts.googleapis.com/css2?family=Open+Sans:wght@400;600&display=swap" rel="stylesheet">
<style>
  :root {
    --navy: #2d3447;
    --paper: #ffffff;
    --ink: #2a2a2a;
    --muted: #555a66;
    --rule: #b9bcc4;
    --backdrop: #d9d9d9;
  }
  * { box-sizing: border-box; margin: 0; padding: 0; }
  html, body {
    width: 1200px; height: 900px; overflow: hidden;
    background: var(--backdrop);
    font-family: "Open Sans", Arial, sans-serif;
    color: var(--ink);
  }
  .sheet {
    width: 1200px; height: 900px;
    display: flex; flex-direction: column;
    align-items: center; justify-content: center; gap: 60px;
  }
  .card {
    width: 600px; height: 343px;
    position: relative; overflow: hidden;
    box-shadow: 0 6px 18px rgba(0,0,0,.18);
  }

  /* Front */
  .card--front { background: var(--navy); }
  .front-panel {
    position: absolute; left: 70px; right: 70px; top: 95px; bottom: 95px;
    background: var(--paper);
    display: flex; align-items: center; justify-content: center;
  }
  .front-frame {
    position: absolute; inset: 8px;
    border: 1px solid var(--ink);
  }
  .brand-name {
    font-weight: 400; font-size: 40px; letter-spacing: 8px;
    color: var(--ink); text-transform: uppercase;
  }

  /* Back */
  .card--back { background: var(--paper); }
  .back-band {
    position: absolute; left: 0; right: 0; top: 0; height: 62px;
    background: var(--navy);
  }
  .contact-row {
    position: absolute; left: 40px; right: 40px; top: 100px;
    display: flex; justify-content: center; gap: 0;
    font-size: 12.5px; line-height: 1.6; color: var(--muted);
  }
  .contact-col { padding: 0 18px; }
  .contact-col + .contact-col { border-left: 1px solid var(--rule); }
  .contact-col--address { text-align: right; }
  .contact-line { display: flex; align-items: center; gap: 7px; white-space: nowrap; }
  .contact-icon { width: 13px; height: 13px; flex: none; }
  .identity {
    position: absolute; left: 0; right: 0; top: 205px;
    text-align: center;
  }
  .person-name { font-size: 20px; font-weight: 400; letter-spacing: .5px; color: var(--ink); }
  .person-degree { font-size: 13px; color: var(--muted); margin-top: 4px; }
  .person-role { font-size: 13px; color: var(--muted); }
</style>
</head>
<body>
<main class="sheet">
  <section class="card card--front" aria-label="Card front">
    <div class="front-panel">
      <div class="front-frame"></div>
      <span class="brand-name">Velotrana</span>
    </div>
  </section>

  <section class="card card--back" aria-label="Card back">
    <div class="back-band"></div>
    <div class="contact-row">
      <div class="contact-col contact-col--address">
        <p>Velotrana AG</p>
        <p>Brunnmattweg 274</p>
        <p>CH-3097 Liebefeld</p>
      </div>
      <div class="contact-col">
        <p class="contact-line">
          <svg class="contact-icon" viewBox="0 0 13 13" aria-hidden="true"><rect width="13" height="13" rx="2" fill="#2d3447"/><rect x="4.5" y="2" width="4" height="9" rx=".8" fill="none" stroke="#fff" stroke-width="1"/></svg>
          +41 79 418 26 97
        </p>
        <p class="contact-line">
          <svg class="contact-icon" viewBox="0 0 13 13" aria-hidden="true"><rect width="13" height="13" rx="2" fill="#2d3447"/><path d="M3.5 3 L5 3 L5.8 5 L4.8 5.8 Q5.8 7.6 7.2 8.3 L8 7.3 L10 8 L10 9.5 Q6.5 10 3.5 6.5 Q3 4.5 3.5 3Z" fill="#fff"/></svg>
          +41 31 742 19 04
        </p>
        <p class="contact-line">
          <svg class="contact-icon" viewBox="0 0 13 13" aria-hidden="true"><rect width="13" height="13" rx="2" fill="#2d3447"/><rect x="3" y="5" width="7" height="5" fill="none" stroke="#fff" stroke-width="1"/><rect x="4.5" y="2.5" width="4" height="2.5" fill="#fff"/></svg>
          +41 31 742 19 38
        </p>
      </div>
      <div class="contact-col">
        <p class="contact-line">
          <svg class="contact-icon" viewBox="0 0 13 13" aria-hidden="true"><rect width="13" height="13" rx="2" fill="#2d3447"/><rect x="2.5" y="3.5" width="8" height="6" fill="none" stroke="#fff" stroke-width="1"/><path d="M2.5 3.5 L6.5 7 L10.5 3.5" fill="none" stroke="#fff" stroke-width="1"/></svg>
          m.ducrante@velotrana.example
        </p>
        <p class="contact-line" style="padding-left:20px">www.velotrana.example</p>
      </div>
    </div>
    <div class="identity">
      <p class="person-name">Marisela DUCRANTE</p>
      <p class="person-degree">M. Law</p>
      <p class="person-role">Managing Partner</p>
    </div>
  </section>
</main>
</body>
</html>
```